Business Card Design

A logo and business card design is required for a new podiatry business based on the Great Ocean Road, Victoria, Australia. The business will provide broad array of podiatry services to communities along the coast.

A distinctive design is sought that represents both professional allied health service delivery and the iconic location of the service, where the ocean meets the Otway ranges. Colours representative of the ocean blues, greens of the local forrest would be desirable.

Target Market(s)

GP's, other allied health professionals, members of the community with foot complaints

Industry/Entity Type

Health

Contact Information for Business Card

Sandstone Heath Podiatry
Declan Hurst
B.Pod B App Sci (HM)
Phone: 0455 731 068
Email: sandstoneheathpodiatry@mailvora.net

Requirements
Must have
• On the back of the card room allocated for appointment times.
Nice to have
• Would like the logo to incorporate a foot and the elements of the coast, whether it be ocean &/or the unique elements of the coast and the great ocean road.

```html
<!DOCTYPE html>
<html lang="en">
<head>
<meta charset="utf-8">
<title>Sandstone Heath Podiatry – Business Card</title>
<link rel="stylesheet" href="https://fonts.googleapis.com/css2?family=Kanit:wght@300;400;500&display=swap">
<style>
  :root {
    --teal: #1aa3a3;
    --ink: #2b2b2b;
    --rule: #3a3a3a;
    --card: #ffffff;
    --backdrop: #eceae6;
    --orange: #ef9421;
  }
  * { margin: 0; padding: 0; box-sizing: border-box; }
  html, body {
    width: 1200px; height: 1000px; overflow: hidden;
    background: var(--backdrop);
    font-family: "Kanit", sans-serif;
  }
  .canvas {
    width: 1200px; height: 1000px;
    display: flex; flex-direction: column; align-items: center;
    justify-content: center; gap: 40px;
  }
  .card {
    width: 700px; height: 400px;
    background: var(--card);
    box-shadow: 0 2px 10px rgba(0,0,0,0.12);
    position: relative;
  }
  /* Front */
  .card-front {
    display: flex; flex-direction: column; align-items: center;
    padding-top: 34px; text-align: center;
  }
  .brand {
    display: flex; align-items: center; gap: 14px;
  }
  .brand-dot {
    width: 22px; height: 22px; border-radius: 50%; background: var(--teal);
  }
  .brand-name {
    font-size: 30px; font-weight: 500; color: var(--teal); letter-spacing: 0.5px;
  }
  .holder-name {
    margin-top: 78px; font-size: 32px; font-weight: 500; color: var(--teal); letter-spacing: 1px;
  }
  .credentials {
    font-size: 20px; font-weight: 300; color: var(--ink); margin-top: -4px;
  }
  .contact {
    margin-top: 30px; display: flex; flex-direction: column; align-items: center; gap: 6px;
  }
  .contact-line { font-size: 26px; font-weight: 300; color: var(--ink); }
  .contact-label { color: var(--teal); font-weight: 400; }
  /* Back */
  .card-back { display: flex; }
  .appointments {
    width: 400px; padding: 36px 30px 36px 40px;
    display: flex; flex-direction: column;
  }
  .appointments-title {
    font-size: 22px; font-weight: 500; color: var(--teal); letter-spacing: 2px;
    margin-bottom: 20px;
  }
  .slot { border-bottom: 2px solid var(--rule); height: 52px; }
  .back-brand {
    flex: 1; display: flex; flex-direction: column; align-items: center;
    justify-content: center; gap: 16px; padding-right: 20px;
  }
  .back-brand .brand-dot { width: 90px; height: 90px; }
  .back-brand .brand-name { font-size: 22px; text-align: center; }
</style>
</head>
<body>
<main class="canvas">
  <section class="card card-front">
    <div class="brand">
      <span class="brand-dot"></span>
      <span class="brand-name">Sandstone Heath Podiatry</span>
    </div>
    <h1 class="holder-name">Declan Hurst</h1>
    <p class="credentials">B.Pod B App Sci (HM)</p>
    <div class="contact">
      <p class="contact-line"><span class="contact-label">Phone:</span>0455 731 068</p>
      <p class="contact-line"><span class="contact-label">Email:</span>sandstoneheathpodiatry@mailvora.net</p>
    </div>
  </section>

  <section class="card card-back">
    <div class="appointments">
      <h2 class="appointments-title">APPOINTMENT</h2>
      <div class="slot"></div>
      <div class="slot"></div>
      <div class="slot"></div>
      <div class="slot"></div>
      <div class="slot"></div>
    </div>
    <div class="back-brand">
      <span class="brand-dot"></span>
      <span class="brand-name">Sandstone Heath Podiatry</span>
    </div>
  </section>
</main>
</body>
</html>
```